Construction Company Website Design

I need a Website Design for a Construction Company. I have attached logo and business card design files (a.i) to match styles and text for the website. I will need design for 3 pages:
1. A Home page
2. A secondary page (will be different information pages)
3. A contact page with submision form
Website to look professional and match the 'theme' across all pages, using main colours / reverse colours as per design files. Must be clear it is a construction related website without being over the top. Happy for the construction related details (whether that be images/outlines/backgrounds etc to be fairly subtle and not overbearing on the contect of the pages. It will be the content that will be most important, not the images within.

Content has not yet been fully completed but attached is a site map. Each page will need a space for the insertion of the relevant heading and associated content for that particular page. Example can be used as per attached map. If it is preferable to have content completed for this to be a more succesful project please advise and I will complete and submit.

Target Market(s)

Clients for potential construction projects. These could be a range of people. All would be very professional, well educated and put a substantial expection on the quality of website provided.

Industry/Entity Type

Construction

Number of Pages Required

3 page

Font styles to use
Serif
Sans Serif
Other font styles liked:
• fonts preferable as per design files provided unless designer beleives a different font would suit better

Requirements
Must have
• Colour scheme to match logo and business card files provided. Fonts that match as per provided files. Pages must be consistent with the theme carrying across all pages. All pages must have contact details at the bottom of the page.
• Contents of page 1 - 'Home page': multiple tab options / logo link
• Contents of page 2 - 'Secondary page': Top and side navigation / area for information and/or images.
• Contents of page - 'Contact us page': Top and side navigation / Submission form / area for logos such as linkdin, facebook etc.
Nice to have
• Would be good to have a or some generic construction related images - outlines / shadows / effects etc. These might be background images or outlines related to the relevant industry and are consistent across the pages. Could be outlines of buildings, images of men with hardhats etc etc. Good to see colour scheme as per design files used
Should not have
• No pictures of houses. Generally no photos. If any imagery of people must not show faces/details.

```html
<!DOCTYPE html>
<html lang="en">
<head>
<meta charset="utf-8">
<title>Kora Constructions</title>
<link rel="stylesheet" href="https://fonts.googleapis.com/css2?family=Roboto:wght@300;400;500;700&display=swap">
<style>
:root{
  --blue:#29a9e9;
  --blue-dark:#1d8fd0;
  --ink:#2a3444;
  --muted:#8a94a3;
  --light:#f3f5f8;
  --line:#dfe3e9;
  --white:#ffffff;
  --hero-a:#3d86ad;
  --hero-b:#2b5f78;
}
*{box-sizing:border-box;margin:0;padding:0}
html,body{width:1200px;height:3509px;overflow:hidden}
body{position:relative;font-family:"Roboto",Helvetica,Arial,sans-serif;color:var(--ink);background:var(--white);font-weight:300}
.abs{position:absolute}
section{position:absolute;left:0;width:1200px}
.eyebrow{position:absolute;font-size:15px;color:var(--muted);font-weight:300}
.heading{position:absolute;font-size:30px;font-weight:400;color:var(--ink)}
.copy{position:absolute;font-size:12.5px;line-height:19px;color:var(--muted)}
/* hero */
.hero{top:0;height:543px;background:linear-gradient(160deg,#4a94bd 0%,var(--hero-a) 35%,#36788f 65%,var(--hero-b) 100%)}
.brand-tab{position:absolute;left:0;top:0;width:300px;height:94px;background:var(--blue);clip-path:polygon(0 0,100% 0,78% 100%,0 100%);display:flex;align-items:center;padding-left:16px}
.brand-name{font-size:17px;font-weight:500;color:var(--white);letter-spacing:1px}
.main-nav{position:absolute;top:40px;left:444px;display:flex;gap:38px}
.main-nav a{color:var(--white);font-size:13px;font-weight:500;text-decoration:none;letter-spacing:.3px}
.hero-phone{position:absolute;top:22px;left:1030px;color:var(--white);font-size:13px;font-weight:500}
.quote-btn{position:absolute;top:56px;left:1022px;width:138px;height:28px;border-radius:14px;background:var(--white);color:var(--blue);font-size:12.5px;font-weight:500;display:flex;align-items:center;justify-content:center}
/* sub bar */
.subbar{top:543px;height:32px;border-bottom:1px solid var(--line);background:var(--white)}
.subbar-links{position:absolute;left:51px;top:9px;font-size:11.5px;color:var(--muted);display:flex;gap:18px}
.subbar-links b{font-weight:400;color:var(--ink)}
.subbar-icons{position:absolute;right:20px;top:8px;display:flex;gap:22px;align-items:center}
.sq{width:15px;height:15px;border-radius:2px}
/* about */
.about{top:575px;height:415px}
.btn{position:absolute;height:37px;border-radius:19px;display:flex;align-items:center;justify-content:center;font-size:13px;font-weight:500}
.btn-solid{background:var(--blue);color:var(--white)}
.btn-ghost{border:1.5px solid var(--line);color:var(--ink)}
.about-visual{position:absolute;left:706px;top:80px;width:403px;height:274px;background:linear-gradient(135deg,#f1f2f4 0%,#d9dde3 55%,#e8c35a 100%);box-shadow:0 6px 18px rgba(0,0,0,.08)}
/* services */
.services{top:990px;height:690px;background:var(--light)}
.service-tab{position:absolute;left:51px;display:flex;align-items:center;gap:16px;font-size:13px;color:var(--muted)}
.service-tab .dot{width:46px;height:46px;border-radius:50%;background:linear-gradient(135deg,#8aa2b5,#3f6178)}
.service-tab.active{background:var(--white);width:298px;height:82px;padding-left:14px;color:var(--blue);box-shadow:0 4px 14px rgba(0,0,0,.05)}
.service-title{position:absolute;left:414px;top:287px;font-size:21px;font-weight:400}
.details-link{position:absolute;left:414px;top:475px;font-size:12px;font-weight:500;color:var(--blue)}
.service-thumb{position:absolute;top:519px;width:200px;height:107px}
/* features */
.features{top:1680px;height:659px}
.center{text-align:center;left:0;width:1200px}
.feature{position:absolute;width:260px}
.feature svg{display:block}
.feature h3{font-size:17px;font-weight:700;margin-top:16px;color:var(--ink)}
.feature p{font-size:12.5px;line-height:20px;color:var(--muted);margin-top:12px}
/* media */
.media{top:2339px;height:643px;background:var(--light)}
.card{position:absolute;top:239px;width:251px;height:353px;background:var(--white)}
.card-photo{width:251px;height:187px}
.card h3{position:absolute;left:20px;top:20px;font-size:17px;font-weight:700;margin-top:187px}
.card p{position:absolute;left:20px;top:245px;width:215px;font-size:12px;line-height:19px;color:var(--muted)}
.card-meta{position:absolute;left:20px;right:20px;top:325px;border-top:1px solid var(--line);padding-top:0;display:flex;justify-content:space-between;font-size:11px;color:var(--ink)}
.card-meta span{margin-top:-7px}
/* contact */
.contact{top:2982px;height:363px}
.col-title{position:absolute;font-size:18px;font-weight:400}
.field{position:absolute;border:1px solid var(--line);border-radius:3px;font-size:11px;color:var(--muted);padding:9px 10px}
.info-line{position:absolute;left:896px;font-size:12px;line-height:19px;color:var(--muted);width:260px}
.social{position:absolute;top:3282px;width:26px;height:26px;border-radius:50%;background:var(--blue)}
/* footer */
.footer{top:3345px;height:164px;border-top:3px solid var(--blue)}
.footer-tab{position:absolute;right:0;top:14px;width:330px;height:48px;background:var(--blue);clip-path:polygon(14% 0,100% 0,100% 100%,0 100%);display:flex;align-items:center;justify-content:flex-end;padding-right:26px}
.footer-links{position:absolute;left:51px;top:46px;display:flex;gap:22px;font-size:12.5px;align-items:center}
.footer-rule{position:absolute;left:51px;right:0;top:75px;border-top:1px solid var(--line)}
.footer-bottom{position:absolute;left:51px;top:90px;display:flex;gap:18px;font-size:11px;color:var(--muted)}
.footer-legal{position:absolute;right:55px;top:90px;display:flex;gap:18px;font-size:11px;color:var(--muted)}
.footer-base{position:absolute;left:0;bottom:0;width:1200px;height:4px;background:var(--blue)}
</style>
</head>
<body>

<section class="hero" role="img" aria-label="Aerial photo of white apartment blocks among pine trees, tinted blue">
  <div class="brand-tab"><span class="brand-name">KORA CONSTRUCTIONS</span></div>
  <nav class="main-nav"><a>SERVICES</a><a>OUR PROJECTS</a><a>CULTURE</a></nav>
  <div class="hero-phone">+1 (800) 555 01 27</div>
  <div class="quote-btn">Request a Quote</div>
</section>

<section class="subbar">
  <div class="subbar-links"><b>Learn More:</b><span>Our Company</span><span>News</span><span>Careers</span><span>Help &amp; Contact</span></div>
  <div class="subbar-icons">
    <span class="sq" style="background:#3b5b98"></span>
    <span class="sq" style="background:#2aa3ef;border-radius:50%"></span>
    <span class="sq" style="background:#d3473a"></span>
    <svg width="14" height="14" viewBox="0 0 14 14"><circle cx="6" cy="6" r="4.5" fill="none" stroke="#55606e" stroke-width="1.6"/><line x1="9.3" y1="9.3" x2="13" y2="13" stroke="#55606e" stroke-width="1.8"/></svg>
  </div>
</section>

<section class="about">
  <div class="eyebrow" style="left:51px;top:37px">About Us</div>
  <h2 class="heading" style="left:51px;top:63px">Who we are ?</h2>
  <p class="copy" style="left:51px;top:123px;width:520px">Sed ut perspiciatis unde omnis iste natus error sit voluptatem accusantium doloremque laudantium, totam rem aperiam.</p>
  <p class="copy" style="left:51px;top:181px;width:520px">Nemo enim ipsam voluptatem quia voluptas sit aspernatur aut odit aut fugit, sed quia consequuntur. Lorem ipsum dolor sit amet, consectetur elnem adipiscing elit.</p>
  <p class="copy" style="left:51px;top:239px;width:520px">sed do eiusmod tempor incididunt ut labore et dolore magna aliqua. Ut enim ad minim veniam, quis nostrud exercitation</p>
  <div class="btn btn-solid" style="left:51px;top:312px;width:162px">Contact Us</div>
  <div class="btn btn-ghost" style="left:250px;top:312px;width:162px">Read More</div>
  <div class="about-visual" role="img" aria-label="Architectural plans with a tablet, glasses, spirit level and a yellow hard hat"></div>
</section>

<section class="services">
  <div class="eyebrow" style="left:51px;top:48px">Services</div>
  <h2 class="heading" style="left:51px;top:72px">What we do ?</h2>
  <p class="copy" style="left:51px;top:142px;width:400px">Sed ut perspiciatis unde omnis iste natus error sit voluptatem Neque porro quisquam est, qui dolorem ipsum quia dolor</p>

  <div class="service-tab active" style="top:245px"><span class="dot" role="img" aria-label="Commercial building thumbnail"></span>Commercial</div>
  <div class="service-tab" style="top:341px;padding-left:14px"><span class="dot" role="img" aria-label="Residential building thumbnail"></span>Residential</div>
  <div class="service-tab" style="top:411px;padding-left:14px"><span class="dot" style="background:linear-gradient(135deg,#e8d9a6,#8c8a6e)" role="img" aria-label="Building maintenance thumbnail"></span>Building Maintenance</div>
  <div class="service-tab" style="top:484px;padding-left:14px"><span class="dot" style="background:linear-gradient(135deg,#e2b45b,#2f5f9a)" role="img" aria-label="Project management thumbnail"></span>Project Management</div>
  <div class="service-tab" style="top:554px;padding-left:14px"><span class="dot" style="background:linear-gradient(135deg,#e6c08a,#b47c45)" role="img" aria-label="Renovations thumbnail"></span>Renovations</div>

  <h3 class="service-title">Commercial Services</h3>
  <p class="copy" style="left:414px;top:330px;width:690px">Sed ut perspiciatis unde omnis iste natus error sit voluptatem accusantium doloremque laudantium, totam rem aperiam, eaque ipsa quae ab illo inventore veritatis et quasi architecto beatae vitae dicta sunt explicabo. Nemo enim ipsam voluptatem quia voluptas sit aspernatur aut odit aut fugit, sed quia consequuntur magni dolores eos qui.</p>
  <p class="copy" style="left:414px;top:409px;width:690px">Sed ut perspiciatis unde omnis iste natus error sit voluptatem accusantium doloremque laudantium, totam rem aperiam, eaque ipsa quae ab illo inventore veritatis et quasi</p>
  <div class="details-link">Details &rsaquo;</div>
  <div class="service-thumb" style="left:414px;background:linear-gradient(135deg,#9bb3a2,#4c6a52)" role="img" aria-label="Aerial view of modern office blocks among trees"></div>
  <div class="service-thumb" style="left:653px;background:linear-gradient(135deg,#6f7f79,#27342f)" role="img" aria-label="Glass building entrance with greenery"></div>
  <div class="service-thumb" style="left:891px;background:linear-gradient(135deg,#8fb7d9,#cfd6cf 60%,#5b7a4d)" role="img" aria-label="White apartment building under blue sky"></div>
</section>

<section class="features">
  <div class="eyebrow center" style="top:50px">Features</div>
  <h2 class="heading center" style="top:83px">Why choose us ?</h2>
  <p class="copy center" style="top:148px;left:400px;width:400px">Sed ut perspiciatis unde omnis iste natus error sit voluptatem Neque porro quisquam est, qui dolorem ipsum quia dolor</p>

  <div class="feature" style="left:194px;top:257px">
    <svg width="64" height="56" viewBox="0 0 64 56" fill="none" stroke="#29a9e9" stroke-width="2.4"><rect x="6" y="18" width="32" height="22"/><path d="M38 26h12l8 8v6H38z"/><circle cx="16" cy="44" r="5" fill="#fff"/><circle cx="48" cy="44" r="5" fill="#fff"/><circle cx="18" cy="10" r="7"/><path d="M18 6v4l3 2"/></svg>
    <h3>Arrival on time</h3>
    <p>Sed ut perspiciatis unde omnis iste natus error sit voluptate accusantium doloremqu.</p>
  </div>
  <div class="feature" style="left:475px;top:257px">
    <svg width="64" height="56" viewBox="0 0 64 56" fill="none" stroke="#29a9e9" stroke-width="2.6"><path d="M12 48L44 12"/><path d="M40 8l10 10"/><path d="M14 10l36 36"/><circle cx="14" cy="10" r="5"/></svg>
    <h3>Professional equipment</h3>
    <p>Nemo qui enim ipsam voluptatem quia voluptas sit aspernatur aut odit aut fugit.</p>
  </div>
  <div class="feature" style="left:755px;top:257px">
    <svg width="64" height="56" viewBox="0 0 64 56" fill="none" stroke="#29a9e9" stroke-width="2.4"><path d="M22 6h20l6 8-16 16-16-16z"/><path d="M16 14h32"/><path d="M10 30v18h44V30"/><path d="M20 40h24"/></svg>
    <h3>Proposition of best solution</h3>
    <p>Sed ut perspiciatis unde omnis iste natus error sit voluptatem quido et.</p>
  </div>
  <div class="feature" style="left:194px;top:456px">
    <svg width="64" height="56" viewBox="0 0 64 56" fill="none" stroke="#29a9e9" stroke-width="2.4"><path d="M6 28c8-12 18-16 26-16s18 4 26 16c-8 12-18 16-26 16S14 40 6 28z"/><circle cx="32" cy="28" r="8"/><circle cx="32" cy="28" r="3" fill="#29a9e9"/></svg>
    <h3>Great sense for detail</h3>
    <p>Sed ut perspiciatis unde omnis iste natus error sit voluptate accusantium doloremqu.</p>
  </div>
  <div class="feature" style="left:475px;top:456px">
    <svg width="64" height="56" viewBox="0 0 64 56" fill="none" stroke="#29a9e9" stroke-width="2.4"><circle cx="32" cy="28" r="16" stroke-dasharray="5 3"/><circle cx="32" cy="28" r="9"/><path d="M32 22l2 4 4 .5-3 3 1 4-4-2-4 2 1-4-3-3 4-.5z" fill="#29a9e9" stroke="none"/></svg>
    <h3>Professional approach</h3>
    <p>Nemo qui enim ipsam voluptatem quia voluptas sit aspernatur aut odit aut fugit.</p>
  </div>
  <div class="feature" style="left:755px;top:456px">
    <svg width="64" height="56" viewBox="0 0 64 56" fill="none" stroke="#29a9e9" stroke-width="2.4"><rect x="16" y="4" width="32" height="46"/><path d="M22 14h20M22 22h20M22 30h20M22 38h12"/><path d="M10 10v44h30"/></svg>
    <h3>Compliance of your plans</h3>
    <p>Sed ut perspiciatis unde omnis iste natus error sit voluptatem quido et.</p>
  </div>
</section>

<section class="media">
  <div class="eyebrow" style="left:51px;top:56px">Media</div>
  <h2 class="heading" style="left:51px;top:82px">Latest News &amp; Views</h2>
  <p class="copy" style="left:51px;top:159px;width:460px">Neque porro quisquam est, qui dolorem ipsum quia dolor sit amet, consectetur, adipisci velit, sed quia non</p>

  <article class="card" style="left:51px">
    <div class="card-photo" style="background:linear-gradient(135deg,#6b4a34,#c6925a 60%,#3a2a20)" role="img" aria-label="Traveller with a leather bag walking on a wooden floor"></div>
    <h3>Standard Post</h3>
    <p>Enim congue blandit. Lorem ipsum dolor sit amet, consectetur adipiscing elit. Quisque...</p>
    <div class="card-meta"><span>&#9638;&nbsp; 22 June, 2015</span><span>&#9646; 0</span></div>
  </article>
  <article class="card" style="left:332px">
    <div class="card-photo" style="background:linear-gradient(135deg,#e8e6e1,#b9b3a7 55%,#4a443d)" role="img" aria-label="Glass pour-over coffee maker on a table"></div>
    <h3>Video Post</h3>
    <p>Ultrices posuere cubilia curae curabitur sit amet tortor ut massa commodo. Vestibulum...</p>
    <div class="card-meta"><span>&#9638;&nbsp; 22 June, 2015</span><span>&#9646; 0</span></div>
  </article>
  <article class="card" style="left:613px">
    <div class="card-photo" style="background:linear-gradient(135deg,#7a4030,#a9684a 50%,#3d2a22)" role="img" aria-label="Cafe interior with brick wall and white chairs"></div>
    <h3>Post with Image</h3>
    <p>Enim congue blandit. Lorem ipsum dolor sit amet, consectetur adipiscing elit. Quisque...</p>
    <div class="card-meta"><span>&#9638;&nbsp; 22 June, 2015</span><span>&#9646; 0</span></div>
  </article>
  <article class="card" style="left:893px">
    <div class="card-photo" style="background:linear-gradient(135deg,#d9d4cc,#a08068 55%,#6a4c38)" role="img" aria-label="Leather wallet resting on a fabric surface"></div>
    <h3>Image Post</h3>
    <p>Ultrices posuere cubilia curae curabitur sit amet tortor ut massa commodo. Vestibulum...</p>
    <div class="card-meta"><span>&#9638;&nbsp; 22 June, 2015</span><span>&#9646; 3</span></div>
  </article>
</section>

<section class="contact">
  <h3 class="col-title" style="left:51px;top:40px">Feel Free to Mail</h3>
  <div class="field" style="left:51px;top:89px;width:117px;height:33px">Name *</div>
  <div class="field" style="left:187px;top:89px;width:117px;height:33px">Email *</div>
  <div class="field" style="left:51px;top:141px;width:253px;height:30px;padding-top:7px">Subject</div>
  <div class="field" style="left:51px;top:192px;width:253px;height:68px">Write Your Message Here...</div>
  <div class="btn btn-solid" style="left:51px;top:283px;width:138px;height:29px;font-size:12px">SEND MESSAGE</div>

  <h3 class="col-title" style="left:332px;width:533px;text-align:center;top:44px">Headquarters</h3>
  <div class="abs" style="left:332px;top:89px;width:533px;height:222px;background:linear-gradient(135deg,#e9ecef 0%,#dfe6dd 45%,#b9d6ef 100%)" role="img" aria-label="Street map of the headquarters area with a location pin"></div>

  <h3 class="col-title" style="left:896px;top:40px">Contact Info</h3>
  <p class="info-line" style="top:84px">Our staff is available to you from 9AM until 5PM on weekdays.</p>
  <p class="info-line" style="top:132px">Phone: +1 (03) 5550 1842</p>
  <p class="info-line" style="top:160px">Office: Harbor Point Gallery</p>
  <p class="info-line" style="top:190px">Email: hello@korabuild.example</p>
  <h3 class="col-title" style="left:896px;top:240px">Follow Us on</h3>
</section>
<span class="social" style="left:900px"></span>
<span class="social" style="left:938px"></span>
<span class="social" style="left:976px"></span>
<span class="social" style="left:1014px"></span>
<span class="social" style="left:1052px"></span>

<footer class="footer" style="position:absolute;left:0;width:1200px">
  <div class="footer-tab"><span class="brand-name" style="font-size:15px">KORA CONSTRUCTIONS</span></div>
  <div class="footer-links">
    <svg width="13" height="13" viewBox="0 0 14 14"><circle cx="6" cy="6" r="4.5" fill="none" stroke="#2a3444" stroke-width="1.6"/><line x1="9.3" y1="9.3" x2="13" y2="13" stroke="#2a3444" stroke-width="1.8"/></svg>
    <span>Help &amp; Contact</span><span>Services</span><span>Our Projects</span><span>Request a Quote</span>
  </div>
  <div class="footer-rule"></div>
  <div class="footer-bottom"><span>About</span><span>News</span><span>Career</span><span>Public Policy</span><span>Culture</span><span>People</span><span>Partners</span></div>
  <div class="footer-legal"><span>&copy; 2005 - 2018</span><span>Privacy</span><span>Legal</span><span>Feedback</span></div>
  <div class="footer-base"></div>
</footer>

</body>
</html>
```